Vorna Fleet business card

I am needing a business card that at a glance shows all the services that we provide emphasizing some more than others. We are a Fleet and Compliance management company as well as a software company. We provide outsourced solutions for KPX compliance and HR services via our own software.
In addition, we do
drug testing
GPS
Cameras
Electronic DVIRS
ELD's

Target Market(s)

Transportation company owners

Industry/Entity Type

Transportation supplier

Contact Information for Business Card

the card should inform potential customers what we do

Other font styles liked:
• I have added brand guidelines. See attached

Requirements
Must have
• See description
Should not have
• Colors outside my brand guide. See attached

```html
<!DOCTYPE html>
<html lang="en">
<head>
<meta charset="utf-8">
<title>Vorna Fleet — Business Card</title>
<link rel="stylesheet" href="https://fonts.googleapis.com/css2?family=Montserrat:wght@400;500;600;700;800&display=swap">
<style>
  :root {
    --stage: #2a2b2d;
    --card: #1c1d1f;
    --card-deep: #161719;
    --pattern-top: #222326;
    --pattern-bottom: #141517;
    --white: #ffffff;
    --red: #ee1d2a;
    --grey: #a8a9ab;
    --rule: #6d6e70;
  }
  * { box-sizing: border-box; margin: 0; padding: 0; }
  html, body {
    width: 1200px;
    height: 1108px;
    overflow: hidden;
    background: var(--stage);
    font-family: "Montserrat", sans-serif;
  }
  .stage {
    position: relative;
    width: 1200px;
    height: 1108px;
  }
  .card {
    position: absolute;
    top: 224px;
    width: 390px;
    height: 660px;
    border-radius: 22px;
    background: var(--card);
    box-shadow: 0 18px 40px rgba(0,0,0,0.45);
    overflow: hidden;
  }
  .card--front { left: 170px; }
  .card--back { left: 640px; }

  /* Front */
  .brand {
    position: absolute;
    top: 118px;
    left: 0;
    right: 0;
    text-align: center;
    color: var(--white);
    font-weight: 800;
    line-height: 1;
  }
  .brand__name { display: block; font-size: 76px; letter-spacing: 1px; }
  .brand__sub { display: block; font-size: 34px; letter-spacing: 22px; margin-top: 14px; padding-left: 22px; }

  .person {
    position: absolute;
    top: 372px;
    left: 0;
    right: 0;
    text-align: center;
  }
  .person__name {
    color: var(--red);
    font-weight: 700;
    font-size: 25px;
    letter-spacing: 0.5px;
  }
  .person__title {
    color: var(--grey);
    font-weight: 500;
    font-size: 19px;
    margin-top: 4px;
  }
  .icon-row {
    position: absolute;
    top: 456px;
    left: 44px;
    right: 44px;
    display: flex;
    align-items: center;
    gap: 10px;
  }
  .icon-row__rule { flex: 1; height: 1px; background: var(--rule); }
  .icon {
    width: 30px;
    height: 30px;
    border-radius: 5px;
    background: var(--red);
    display: flex;
    align-items: center;
    justify-content: center;
  }
  .icon svg { width: 20px; height: 20px; }
  .contact {
    position: absolute;
    top: 500px;
    left: 0;
    right: 0;
    text-align: center;
    color: var(--grey);
    font-size: 18px;
    line-height: 1.45;
  }
  .contact__rule {
    position: absolute;
    top: 586px;
    left: 66px;
    right: 66px;
    height: 1px;
    background: var(--rule);
  }
  .address {
    position: absolute;
    top: 598px;
    left: 0;
    right: 0;
    text-align: center;
    color: var(--grey);
    font-size: 18px;
    line-height: 1.35;
  }

  /* Back */
  .card__texture {
    position: absolute;
    inset: 0;
    background: linear-gradient(160deg, var(--pattern-top), var(--pattern-bottom));
  }
  .back-brand {
    position: absolute;
    top: 318px;
    left: 0;
    right: 0;
    text-align: center;
    color: var(--white);
    font-weight: 800;
    font-size: 34px;
    letter-spacing: 0.5px;
  }
  .services {
    position: absolute;
    top: 404px;
    left: 0;
    right: 0;
    text-align: center;
    color: var(--white);
    font-weight: 500;
    font-size: 19px;
    line-height: 1.7;
    letter-spacing: 0.3px;
  }
  .services__dot {
    display: inline-block;
    width: 10px;
    height: 10px;
    border-radius: 50%;
    background: var(--red);
    margin: 0 8px;
    vertical-align: middle;
    position: relative;
    top: -2px;
  }
</style>
</head>
<body>
<main class="stage">

  <section class="card card--front" aria-label="Business card front">
    <h1 class="brand">
      <span class="brand__name">VORNA</span>
      <span class="brand__sub">FLEET</span>
    </h1>

    <div class="person">
      <p class="person__name">JONATHAN SMITH</p>
      <p class="person__title">Managing Director</p>
    </div>

    <div class="icon-row">
      <span class="icon-row__rule"></span>
      <span class="icon" aria-label="Phone">
        <svg viewBox="0 0 24 24" fill="none" stroke="#1c1d1f" stroke-width="2" stroke-linejoin="round">
          <path d="M4 9c0-3 3-4 8-4s8 1 8 4l-3 1-1-2H8l-1 2z"/>
          <rect x="6" y="12" width="12" height="7" rx="1"/>
        </svg>
      </span>
      <span class="icon" aria-label="Email">
        <svg viewBox="0 0 24 24" fill="none" stroke="#1c1d1f" stroke-width="2" stroke-linejoin="round">
          <rect x="3" y="6" width="18" height="12" rx="1"/>
          <path d="M3 6l9 7 9-7M3 18l7-6M21 18l-7-6"/>
        </svg>
      </span>
      <span class="icon" aria-label="Website">
        <svg viewBox="0 0 24 24" fill="none" stroke="#1c1d1f" stroke-width="2">
          <circle cx="12" cy="12" r="8"/>
          <path d="M4 12h16M12 4c3 3 3 13 0 16M12 4c-3 3-3 13 0 16"/>
        </svg>
      </span>
      <span class="icon-row__rule"></span>
    </div>

    <address class="contact" style="font-style:normal">
      044-123 456 789<br>
      info@webname.com<br>
      www.websitename.com
    </address>
    <span class="contact__rule"></span>
    <address class="address" style="font-style:normal">
      421, Address line here<br>
      45452, Country Name
    </address>
  </section>

  <section class="card card--back" aria-label="Business card back">
    <div class="card__texture" role="img" aria-label="Subtle tone-on-tone repeating brand pattern covering the card"></div>
    <p class="back-brand">VORNA</p>
    <p class="services">
      DRUG TESTING<span class="services__dot"></span>GPS<span class="services__dot"></span>CAMERAS<br>
      ELECTRONIC DVIRS<span class="services__dot"></span>ELD'S
    </p>
  </section>

</main>
</body>
</html>
```